We need a letterhead design for a new international company based in Luanda, Angola called "Solmarin Corporation". Solmarin Corporation is a multiservice private company. We provides services for the following sectors: Oil & Gas industry, Government, and the Public.

Target Market(s)

Board of directors of the following sectors: Oil & Gas industry, Government, and the Public.

Industry/Entity Type

Government

Requirements
Must have
• Solmarin Corporation logo

```html
<!DOCTYPE html>
<html lang="en">
<head>
<meta charset="utf-8">
<title>Solmarin Corporation Letterhead</title>
<link href="https://fonts.googleapis.com/css2?family=Open+Sans:wght@400;600;700&display=swap" rel="stylesheet">
<style>
  :root {
    --backdrop: #e4e4e4;
    --paper: #ffffff;
    --paper-shade-top: #f3f3f3;
    --paper-shade-bottom: #b9b9b9;
    --ink: #2a2a2a;
    --ink-soft: #4a4a4a;
    --footer-ink: #5a5a5a;
    --brand-gold: #c9962a;
  }
  * { box-sizing: border-box; margin: 0; padding: 0; }
  html, body { width: 1200px; height: 720px; overflow: hidden; }
  body {
    background: var(--backdrop);
    font-family: "Open Sans", sans-serif;
    color: var(--ink);
    position: relative;
  }
  .sheet {
    position: absolute;
    top: 50px;
    width: 480px;
    height: 620px;
    box-shadow: 0 4px 14px rgba(0,0,0,0.18);
  }
  .sheet--cover {
    left: 90px;
    background: linear-gradient(180deg, var(--paper-shade-top) 0%, #d2d2d2 55%, var(--paper-shade-bottom) 100%);
  }
  .sheet--letter {
    left: 630px;
    background: var(--paper);
  }
  .brand {
    display: flex;
    align-items: center;
    gap: 8px;
  }
  .brand__mark {
    border-radius: 50%;
    background: var(--brand-gold);
    flex: none;
  }
  .brand__name {
    font-weight: 700;
    color: var(--ink);
    letter-spacing: 0.3px;
    white-space: nowrap;
  }
  .sheet--cover .brand {
    position: absolute;
    left: 34px;
    bottom: 62px;
  }
  .sheet--cover .brand__mark { width: 28px; height: 28px; }
  .sheet--cover .brand__name { font-size: 22px; }
  .contact-line {
    position: absolute;
    left: 34px;
    bottom: 34px;
    display: flex;
    gap: 18px;
    font-size: 9px;
    color: var(--footer-ink);
  }
  .contact-line__item { display: flex; align-items: center; gap: 5px; }
  .contact-line svg { width: 9px; height: 9px; fill: var(--brand-gold); }

  .sheet--letter .brand {
    position: absolute;
    top: 44px;
    left: 0; right: 0;
    justify-content: center;
  }
  .sheet--letter .brand__mark { width: 20px; height: 20px; }
  .sheet--letter .brand__name { font-size: 15px; }

  .letter {
    position: absolute;
    top: 112px;
    left: 54px;
    right: 54px;
    font-size: 8.6px;
    line-height: 1.32;
    color: var(--ink-soft);
  }
  .recipient { margin-bottom: 16px; font-style: normal; }
  .recipient__name { font-weight: 700; color: var(--ink); }
  .letter__body p { text-align: justify; margin-bottom: 10px; }
  .letter__closing { margin-top: 4px; }
  .signature { margin-top: 40px; }
  .signature__name { font-weight: 700; color: var(--ink); }
</style>
</head>
<body>
  <section class="sheet sheet--cover">
    <div class="brand">
      <span class="brand__mark"></span>
      <span class="brand__name">Solmarin Corporation</span>
    </div>
    <div class="contact-line">
      <span class="contact-line__item">
        <svg viewBox="0 0 10 10"><path d="M2 0.5 L3.6 0.5 L4.4 2.8 L3.3 3.7 Q4.2 5.8 6.3 6.7 L7.2 5.6 L9.5 6.4 L9.5 8 Q9.5 9.5 8 9.5 Q0.5 9 0.5 2 Q0.5 0.5 2 0.5 Z"/></svg>
        800 555 0142
      </span>
      <span class="contact-line__item">
        <svg viewBox="0 0 10 10"><path d="M5 0 A3.6 3.6 0 0 1 8.6 3.6 Q8.6 6 5 10 Q1.4 6 1.4 3.6 A3.6 3.6 0 0 1 5 0 Z M5 2.3 A1.3 1.3 0 1 0 5 4.9 A1.3 1.3 0 1 0 5 2.3 Z"/></svg>
        48 Harbor Ave. Milton, SC 2740
      </span>
    </div>
  </section>

  <section class="sheet sheet--letter">
    <div class="brand">
      <span class="brand__mark"></span>
      <span class="brand__name">Solmarin Corporation</span>
    </div>
    <div class="letter">
      <address class="recipient">
        <div class="recipient__name">Mr. Daniel Reyes</div>
        <div>Managing Director</div>
        <div>MA Investor</div>
        <div>240 W Harbor Street</div>
        <div>USA</div>
      </address>
      <div class="letter__body">
        <p>Lorem Ipsum is simply dummy text for printing and typesetting industry. Lorem Ipsum has been the industry's standard dummy text since the 1500s, when an unknown printer took a galley of type and scrambled it to make a type specimen book. It has survived not only manual work but also the leap into electronic typesetting, remaining essentially unchanged. It was popularised in the 1960s with the release of transfer lettering sheets containing Lorem Ipsum passages and more recently with page layout software including version 6.9 of Lorem Ipsum.</p>
        <p>Contrary to popular belief, Lorem Ipsum is not simply random text. It has roots in a piece of classical Latin literature from 45 BC, making it over 2000 years old. A Latin professor at a small college looked up one of the more obscure words in a classical passage and discovered the undoubtable source. Lorem Ipsum comes from sections 1.10.32 and 1.10.33 of a treatise on the extremes of good and evil by an ancient author, written in 45 BC. This book on the theory of ethics was very popular during the Renaissance.</p>
        <p class="letter__closing">Thank you for being one of our valued customers.</p>
      </div>
      <div class="signature">
        <div class="signature__name">Name Here</div>
        <div>CEO</div>
      </div>
    </div>
  </section>
</body>
</html>
```